A weight loss and fitness website design

I am into different types of modern weight loss techniques for people who are a little fatty and wish to be physically and mentally fit. Basically, the website is to teach people how to reduce weight using different methods such as diet, exercises, yoga and other forms. I would need an eye catching website which would make visitors want to come back. The will be also be different forms of exercises for a health and fit life. This said, my website is to have two categories of
1) weight loss techniques
2) exercise of fit and healthy living.
I prefer bright colors such as green, blue, yellow, and orange. Imagery should include before and after pictures of people suffering from obesity, people under going exercises.
Designers can get ideas and inspiration from the website quimtary.com which i was previously part of the team.
Target Market(s)
My target audience are people suffering from obesity, malnutrition and physical deficiency.
Industry/Entity Type
Fitness
Coding
Coded - Design and coding required
Number of Pages Required
1 page
Look and feel
Each slider illustrates characteristics of the customer's brand and the style your logo design should communicate.

```html
<!DOCTYPE html>
<html lang="en">
<head>
<meta charset="utf-8">
<title>Halvera Fitness</title>
<link href="https://fonts.googleapis.com/css2?family=Montserrat:wght@400;600;700;800&family=Open+Sans:wght@400;600;700&family=Roboto+Condensed:wght@700&display=swap" rel="stylesheet">
<style>
:root{
  --orange:#f47a20;
  --orange-deep:#e8641a;
  --blue:#1464b4;
  --blue-deep:#0f4f95;
  --yellow:#f8a91c;
  --ink:#1b1b1b;
  --text:#555;
  --light:#f2f2f2;
  --dark:#111214;
  --white:#fff;
}
*{box-sizing:border-box;margin:0;padding:0}
html,body{width:1200px;height:3383px;overflow:hidden}
body{font-family:"Open Sans",Arial,sans-serif;color:var(--text);background:var(--white);position:relative}
.section{position:absolute;left:0;width:1200px;overflow:hidden}
.btn{display:inline-block;font-family:"Open Sans",Arial,sans-serif;font-weight:700;text-transform:uppercase;color:var(--white);background:var(--yellow);border-radius:2px;text-align:center}
.photo{position:absolute}

/* header */
.hero{top:0;height:545px;background:var(--orange)}
.hero .photo{left:330px;top:0;width:870px;height:545px;background:linear-gradient(120deg,#5a8fb3 0%,#2d5f86 45%,#c98a6a 60%,#2a4a6b 100%)}
.hero svg.shapes{position:absolute;left:0;top:0}
.topbar{position:absolute;top:0;left:0;width:1200px;height:34px}
.nav{position:absolute;right:0;top:0;height:34px;width:760px;background:var(--dark);display:flex;align-items:center;padding-left:70px;gap:34px;font-size:13px;font-weight:600}
.nav a{color:var(--orange);text-decoration:none}
.nav a.active{color:var(--white)}
.nav .search{position:absolute;right:70px;top:10px}
.logo{position:absolute;left:130px;top:22px;font-family:"Roboto Condensed",Arial,sans-serif;font-weight:700;font-size:33px;color:var(--blue)}
.hero-copy{position:absolute;left:180px;top:222px;color:var(--white)}
.hero-copy h1{font-family:"Montserrat",Arial,sans-serif;font-weight:700;font-size:34px;line-height:41px;border-top:4px solid var(--white);padding-top:10px;display:inline-block}
.hero-copy h2{font-family:"Montserrat",Arial,sans-serif;font-weight:700;font-size:18px;margin-top:8px}
.hero-copy p{font-size:10.5px;line-height:16px;width:230px;margin-top:14px}
.hero-copy .btn{margin-top:20px;padding:10px 14px;font-size:12px}

/* intro */
.intro{top:545px;height:430px;background:var(--white);text-align:center}
.intro h2{font-family:"Open Sans",Arial,sans-serif;font-weight:600;font-size:20px;color:var(--ink);line-height:26px;margin-top:37px}
.intro .lead{font-size:11.5px;color:#444;margin-top:8px}
.intro h3{font-family:"Open Sans",Arial,sans-serif;font-weight:600;font-size:19px;color:var(--orange-deep);margin-top:20px}
.category{position:absolute;width:310px;height:205px;top:178px;text-align:center}
.category.first{left:270px;background:#eeeeee;box-shadow:0 8px 10px rgba(0,0,0,.12)}
.category.second{left:620px}
.category .icon{position:absolute;left:122px;top:20px;width:66px;height:66px}
.category .num{position:absolute;top:50px;width:26px;height:26px;border-radius:50%;color:#fff;font-size:12px;font-weight:700;line-height:26px}
.category h4{font-weight:400;font-size:15px;color:#444;position:absolute;left:0;width:100%;top:102px}
.category .btn{position:absolute;left:109px;top:135px;width:92px;padding:7px 0;font-size:11px;text-transform:none;font-weight:400}
.intro svg.link{position:absolute;left:520px;top:140px}

/* personal training */
.plans{top:975px;height:453px;background:var(--blue)}
.plans .photo{left:0;top:0;width:760px;height:453px;background:linear-gradient(100deg,#e9a98a 0%,#f2d2c2 30%,#c9b9ae 55%,#8f7f76 100%);clip-path:polygon(0 0,420px 0,760px 453px,0 453px)}
.plans svg.shapes{position:absolute;left:0;top:0}
.plans-copy{position:absolute;left:726px;top:88px;color:var(--white)}
.plans-copy h2{font-family:"Montserrat",Arial,sans-serif;font-weight:700;font-size:33px;line-height:40px;border-top:4px solid var(--white);padding-top:10px;width:300px}
.plans-copy p{font-size:11.5px;line-height:17px;width:310px;margin-top:10px}
.plans-copy .plan{font-size:13px;margin-top:18px}
.plans-copy .price{font-family:"Montserrat",Arial,sans-serif;font-weight:700;font-size:27px;margin-top:6px}
.plans-copy .price small{font-size:12px;font-weight:600}
.plans-copy .btn{position:absolute;left:178px;top:278px;padding:10px 16px;font-size:12px}
.dots{display:flex;gap:7px;justify-content:center}
.dots i{width:8px;height:8px;border-radius:50%;background:#ccc;display:block}
.dots i.on{background:var(--yellow)}
.plans .dots{position:absolute;left:968px;top:350px}
.plans .dots i{background:#fff}
.plans .dots i.on{background:var(--yellow)}

/* classes */
.classes{top:1428px;height:512px;background:linear-gradient(135deg,var(--orange) 0%,#f68a30 50%,var(--orange-deep) 100%)}
.section-title{font-family:"Montserrat",Arial,sans-serif;font-weight:700;font-size:32px;text-align:center;text-transform:uppercase}
.section-title::after{content:"";display:block;width:36px;height:3px;background:var(--orange);margin:6px auto 0}
.classes .section-title{color:var(--white);margin-top:28px}
.classes .section-title::after{background:var(--white)}
.class-card{position:absolute;top:100px;width:304px;height:352px;background:#f6f6f6;box-shadow:0 6px 10px rgba(0,0,0,.15)}
.class-card .photo{left:0;top:0;width:304px;height:190px}
.class-card .caption{position:absolute;left:0;top:135px;width:100%;text-align:center;color:#fff}
.class-card .caption b{display:block;font-family:"Montserrat",Arial,sans-serif;font-size:14px}
.class-card .caption span{font-size:13px}
.class-card .glyph{position:absolute;left:137px;top:96px}
.class-card p{position:absolute;left:18px;top:208px;width:270px;font-size:10.5px;line-height:16px;color:#444}
.class-card .rule{position:absolute;left:18px;right:18px;top:274px;border-top:1px dashed #bbb}
.class-card .label{position:absolute;left:18px;top:284px;font-size:12px;font-weight:700;color:#333}
.class-card .fee{position:absolute;right:20px;top:280px;font-size:24px;font-weight:600;color:#333}
.class-card .btn{position:absolute;left:18px;top:308px;padding:6px 9px;font-size:10px}
.class-card .sessions{position:absolute;right:20px;top:316px;font-size:11px;color:#444}
.classes .dots{position:absolute;left:0;width:100%;top:476px}
.classes .dots i{background:#fff}
.classes .dots i.on{background:var(--yellow)}

/* before after */
.results{top:1940px;height:430px;background:linear-gradient(180deg,#f4f4f4,#ececec)}
.results .section-title{color:var(--ink);margin-top:26px}
.shot{position:absolute;top:106px;width:203px;height:237px;box-shadow:0 4px 10px rgba(0,0,0,.15)}
.shot-label{position:absolute;top:356px;width:203px;text-align:center;font-size:20px;color:#666;font-weight:600}
.results .dots{position:absolute;left:0;width:100%;top:392px}

/* testimonials */
.testimonials{top:2370px;height:500px;background:var(--white)}
.testimonials .section-title{color:var(--ink);margin-top:32px}
.quote-card{position:absolute;top:112px;width:300px;height:316px;background:var(--white);box-shadow:0 3px 12px rgba(0,0,0,.14);text-align:center}
.quote-card .head{height:88px;background:#f0f0f0}
.quote-card h4{font-weight:400;font-size:15px;color:#222;padding-top:14px}
.quote-card .avatar{position:absolute;left:107px;top:42px;width:86px;height:86px;border-radius:50%;border:3px solid #fff}
.quote-card p{position:absolute;left:26px;width:248px;top:150px;font-size:11.5px;line-height:18px;color:#333}
.quote-card .btn{position:absolute;left:113px;top:254px;padding:5px 12px;font-size:10px;text-transform:none;font-weight:400}
.testimonials .dots{position:absolute;left:0;width:100%;top:452px}

/* join */
.join{top:2870px;height:142px;background:#e7e7e7}
.join h2{position:absolute;left:296px;top:45px;font-family:"Montserrat",Arial,sans-serif;font-weight:700;font-size:32px;color:var(--ink)}
.join p{position:absolute;left:232px;top:83px;font-size:12px;color:#333}
.join .field{position:absolute;left:458px;top:59px;width:298px;height:38px;background:#fff;font-size:11px;color:#777;padding:12px 16px}
.join .field svg{position:absolute;right:14px;top:13px}
.join .btn{position:absolute;left:768px;top:59px;width:122px;height:38px;line-height:38px;font-size:13px;text-transform:uppercase;font-weight:600}

/* contact */
.contact{top:3012px;height:308px}
.contact .left{position:absolute;left:0;top:0;width:610px;height:308px;background:var(--blue)}
.contact .left .photo{left:180px;top:0;width:430px;height:308px;background:radial-gradient(ellipse at 55% 40%,rgba(10,50,100,.55),rgba(20,100,180,0) 70%)}
.contact .right{position:absolute;left:610px;top:0;width:590px;height:308px;background:var(--orange)}
.contact .right .photo{left:0;top:0;width:590px;height:308px;background:linear-gradient(135deg,rgba(255,255,255,.08),rgba(0,0,0,.05))}
.contact h3{font-family:"Open Sans",Arial,sans-serif;font-weight:600;font-size:15px;color:#fff;text-transform:uppercase}
.form{position:absolute;left:226px;top:28px}
.form input,.form .area{display:block;width:244px;height:28px;margin-top:10px;border:1px solid #fff;background:transparent;color:#fff;font-size:11px;padding:0 10px;font-family:inherit}
.form .area{height:50px;padding-top:6px}
.form .send{display:block;margin-top:12px;width:244px;height:36px;line-height:36px;font-size:13px;text-transform:uppercase;font-weight:400}
.info{position:absolute;left:52px;top:22px;color:#fff}
.info .brand{font-family:"Roboto Condensed",Arial,sans-serif;font-weight:700;font-size:32px;margin-top:8px}
.info .address{position:absolute;left:0;top:106px;padding-left:26px;font-size:10px;line-height:16px;width:200px}
.info .reach{position:absolute;left:190px;top:106px;font-size:10.5px;line-height:28px;padding-left:26px;width:220px}
.info svg{position:absolute}
.social{position:absolute;left:40px;top:196px;display:flex;gap:10px}
.social i{display:block;width:30px;height:30px;background:var(--dark)}

/* footer */
.footer{top:3320px;height:63px;background:var(--dark)}
.footer nav{position:absolute;left:156px;top:23px;display:flex;gap:26px;font-size:13px;font-weight:600}
.footer nav a{color:var(--orange);text-decoration:none}
.footer nav a.active{color:#fff}
.footer .copy{position:absolute;right:180px;top:24px;font-size:11px;color:#aaa}
</style>
</head>
<body>

<header class="section hero">
  <div class="photo" role="img" aria-label="Photo of a muscular man and a woman holding dumbbells"></div>
  <svg class="shapes" width="1200" height="545" viewBox="0 0 1200 545">
    <polygon points="0,0 540,0 360,545 0,545" fill="#f47a20"/>
    <polygon points="300,0 540,0 360,545 250,545" fill="#f68a30"/>
    <polygon points="1000,0 1200,0 1200,545 1060,545" fill="#1464b4" opacity=".55"/>
    <polygon points="110,0 350,0 230,142" fill="#ffffff"/>
  </svg>
  <div class="topbar">
    <nav class="nav">
      <a class="active" href="#">Home</a><a href="#">About Us</a><a href="#">Training</a><a href="#">Classes</a><a href="#">Contact Us</a><a href="#">Testimonials</a>
      <svg class="search" width="13" height="13" viewBox="0 0 13 13"><circle cx="5.5" cy="5.5" r="4" fill="none" stroke="#fff" stroke-width="2"/><line x1="8.5" y1="8.5" x2="12" y2="12" stroke="#fff" stroke-width="2"/></svg>
    </nav>
  </div>
  <div class="logo">Halvera Fitness</div>
  <div class="hero-copy">
    <h1>CHANGE<br>YOUR LIFE</h1>
    <h2>HALVERA FITNESS</h2>
    <p>We provide modern weight loss techniques for people who are a little fatty and wish to be physically and mentally fit.</p>
    <a class="btn" href="#">Get Started</a>
  </div>
</header>

<section class="section intro">
  <h2>We offer a wide variety of trainings to<br>achieve the best results</h2>
  <p class="lead">We teach people how to reduce weight using different methods such as diet, exercises, yoga and other forms.</p>
  <h3>There will be 2 categories</h3>
  <svg class="link" width="200" height="130" viewBox="0 0 200 130">
    <path d="M30 110 C 60 110, 80 80, 80 40 C 80 10, 100 10, 110 40 C 120 90, 150 110, 186 118" fill="none" stroke="#444" stroke-width="1.5" stroke-dasharray="4 4"/>
  </svg>
  <div class="category first">
    <svg class="icon" viewBox="0 0 66 66"><rect x="10" y="14" width="46" height="44" rx="6" fill="#e8641a"/><circle cx="33" cy="34" r="11" fill="#fff"/><line x1="33" y1="34" x2="38" y2="27" stroke="#e8641a" stroke-width="2.5"/><rect x="24" y="8" width="18" height="8" rx="2" fill="#e8641a"/></svg>
    <span class="num" style="left:208px;background:#e8641a">1</span>
    <h4>Weight loss techniques</h4>
    <a class="btn" href="#" style="background:#e8641a">Read more</a>
  </div>
  <div class="category second">
    <svg class="icon" viewBox="0 0 66 66"><circle cx="33" cy="14" r="6" fill="#1464b4"/><path d="M33 22 L33 40 M33 26 L18 34 M33 26 L48 34 M16 50 Q33 38 50 50 Z" stroke="#1464b4" stroke-width="5" stroke-linecap="round" fill="#1464b4"/></svg>
    <span class="num" style="left:88px;background:#1464b4">2</span>
    <h4>Exercise of fit and healthy living</h4>
    <a class="btn" href="#" style="background:#1464b4">Read more</a>
  </div>
</section>

<section class="section plans">
  <div class="photo" role="img" aria-label="Photo of two smiling women working out with dumbbells"></div>
  <svg class="shapes" width="1200" height="453" viewBox="0 0 1200 453">
    <polygon points="0,0 140,0 0,230" fill="#f47a20" opacity=".75"/>
    <polygon points="0,453 0,330 90,453" fill="#f47a20" opacity=".6"/>
    <polygon points="420,0 560,0 760,453 690,453" fill="#0f4f95" opacity=".5"/>
  </svg>
  <div class="plans-copy">
    <h2>PERSONAL<br>TRAINING PLANS</h2>
    <p>Lorem ipsum dolor sit amet, consectetur adipiscing elit. Integer at nisl quam. Pellentesque gravida nec tortor condimentum tempus morbi eget lacus eros.</p>
    <div class="plan">Beginner Plan Basic</div>
    <div class="price">$39.99 <small>/ month</small></div>
    <a class="btn" href="#">Sign up now</a>
  </div>
  <div class="dots"><i class="on"></i><i></i><i></i></div>
</section>

<section class="section classes">
  <h2 class="section-title">Classes</h2>

  <article class="class-card" style="left:131px">
    <div class="photo" role="img" aria-label="Photo of women doing a floor workout class" style="background:linear-gradient(160deg,#8f7fa0,#4b4f63)"></div>
    <svg class="glyph" width="30" height="30" viewBox="0 0 30 30"><rect x="4" y="8" width="22" height="20" rx="4" fill="#fff"/><rect x="10" y="3" width="10" height="6" rx="1" fill="#fff"/></svg>
    <div class="caption"><b>MARISA KOVEL</b><span>Weight Loss Training class</span></div>
    <p>Lorem ipsum dolor sit amet, consectetur adipiscing elit. Integer at nisl quam. Pellentesque gravida nec tortor condimentum tempus morbi eget lacus eros.</p>
    <div class="rule"></div>
    <div class="label">Training Price</div><div class="fee">$60</div>
    <a class="btn" href="#">Sign up</a><div class="sessions">1 - 5 sessions / month</div>
  </article>

  <article class="class-card" style="left:449px">
    <div class="photo" role="img" aria-label="Photo of a woman in a yoga pose" style="background:linear-gradient(160deg,#6a6c70,#2d2f33)"></div>
    <svg class="glyph" width="30" height="30" viewBox="0 0 30 30"><circle cx="15" cy="5" r="3.5" fill="#fff"/><path d="M15 10 V19 M15 12 L5 17 M15 12 L25 17 M4 26 Q15 18 26 26 Z" stroke="#fff" stroke-width="3" fill="#fff" stroke-linecap="round"/></svg>
    <div class="caption"><b>MARISA KOVEL</b><span>Yoga Training class</span></div>
    <p>Lorem ipsum dolor sit amet, consectetur adipiscing elit. Integer at nisl quam. Pellentesque gravida nec tortor condimentum tempus morbi eget lacus eros.</p>
    <div class="rule"></div>
    <div class="label">Training Price</div><div class="fee">$60</div>
    <a class="btn" href="#">Sign up</a><div class="sessions">1 - 5 sessions / month</div>
  </article>

  <article class="class-card" style="left:767px">
    <div class="photo" role="img" aria-label="Photo of a woman holding a dumbbell and a plate of vegetables" style="background:linear-gradient(160deg,#d8d2d2,#a89c9c)"></div>
    <svg class="glyph" width="30" height="30" viewBox="0 0 30 30"><path d="M8 3 V12 Q8 15 10 15 V28 M6 3 V10 M12 3 V10 M21 3 Q26 8 22 15 V28" stroke="#fff" stroke-width="3" fill="none" stroke-linecap="round"/></svg>
    <div class="caption"><b>MARISA KOVEL</b><span>Diet Training class</span></div>
    <p>Lorem ipsum dolor sit amet, consectetur adipiscing elit. Integer at nisl quam. Pellentesque gravida nec tortor condimentum tempus morbi eget lacus eros.</p>
    <div class="rule"></div>
    <div class="label">Training Price</div><div class="fee">$60</div>
    <a class="btn" href="#">Sign up</a><div class="sessions">1 - 5 sessions / month</div>
  </article>

  <div class="dots"><i class="on"></i><i></i><i></i></div>
</section>

<section class="section results">
  <h2 class="section-title">Before - After</h2>
  <div class="shot" style="left:153px;background:linear-gradient(180deg,#fff 0%,#f0d0b8 40%,#4a5a80 85%,#fff 100%)" role="img" aria-label="Before photo of a woman in an orange top"></div>
  <div class="shot" style="left:381px;background:linear-gradient(180deg,#fff 0%,#f2d6bf 40%,#4a5a80 85%,#fff 100%)" role="img" aria-label="After photo of the same woman, slimmer, arms raised"></div>
  <div class="shot" style="left:611px;background:linear-gradient(180deg,#e4e4e4 0%,#2a2a2a 25%,#f5f5f5 55%,#2e2e3a 100%)" role="img" aria-label="Before photo of a heavier woman in a white shirt, side view"></div>
  <div class="shot" style="left:841px;background:linear-gradient(180deg,#e4e4e4 0%,#2a2a2a 25%,#f5f5f5 55%,#2e2e3a 100%)" role="img" aria-label="After photo of the same woman, slimmer, side view"></div>
  <div class="shot-label" style="left:153px">Before</div>
  <div class="shot-label" style="left:381px">After</div>
  <div class="shot-label" style="left:611px">Before</div>
  <div class="shot-label" style="left:841px">After</div>
  <div class="dots"><i class="on"></i><i></i><i></i></div>
</section>

<section class="section testimonials">
  <h2 class="section-title">Testimonials</h2>
  <article class="quote-card" style="left:131px">
    <div class="head"><h4>AUTHOR NAME</h4></div>
    <div class="avatar" role="img" aria-label="Portrait of a woman with auburn hair" style="background:#b86a48"></div>
    <p>“ Vestibulum a imperdiet imperdiet placerat a ullamcorper a vestibulum nibh in enim himenaeos tempus metus in rhoncus.Porttitor vestibulum sapien arcu. ”</p>
    <a class="btn" href="#">Read more</a>
  </article>
  <article class="quote-card" style="left:447px">
    <div class="head"><h4>AUTHOR NAME</h4></div>
    <div class="avatar" role="img" aria-label="Portrait of a young man with dark hair" style="background:#4a3a30"></div>
    <p>“ Vestibulum a imperdiet imperdiet placerat a ullamcorper a vestibulum nibh in enim himenaeos tempus metus in rhoncus.Porttitor vestibulum sapien arcu. ”</p>
    <a class="btn" href="#">Read more</a>
  </article>
  <article class="quote-card" style="left:762px">
    <div class="head"><h4>AUTHOR NAME</h4></div>
    <div class="avatar" role="img" aria-label="Portrait of a smiling woman with dark hair" style="background:#c9a08a"></div>
    <p>“ Vestibulum a imperdiet imperdiet placerat a ullamcorper a vestibulum nibh in enim himenaeos tempus metus in rhoncus.Porttitor vestibulum sapien arcu. ”</p>
    <a class="btn" href="#">Read more</a>
  </article>
  <div class="dots"><i class="on"></i><i></i><i></i></div>
</section>

<section class="section join">
  <h2>JOIN US</h2>
  <p>SIGN UP FOR OUR NEWS LETTER</p>
  <div class="field">ENTER EMAIL ID
    <svg width="14" height="11" viewBox="0 0 14 11"><rect x=".5" y=".5" width="13" height="10" fill="none" stroke="#999"/><path d="M.5 .5 L7 6 L13.5 .5" fill="none" stroke="#999"/></svg>
  </div>
  <a class="btn" href="#">Subscribe</a>
</section>

<section class="section contact">
  <div class="left">
    <div class="photo" role="img" aria-label="Faded photo of a man exercising"></div>
    <form class="form">
      <h3>Get in touch</h3>
      <input type="text" placeholder="Enter your name" value="Enter your name">
      <input type="text" value="Phone Number">
      <input type="text" value="Email">
      <div class="area">Comment</div>
      <span class="btn send">Send your enquire &nbsp;➤</span>
    </form>
  </div>
  <div class="right">
    <div class="photo" role="img" aria-label="Faint street map in orange tones"></div>
    <div class="info">
      <h3>Contact info</h3>
      <div class="brand">Halvera Fitness</div>
      <svg width="12" height="16" viewBox="0 0 12 16" style="left:0;top:108px"><path d="M6 0 C2.7 0 0 2.6 0 6 C0 10 6 16 6 16 C6 16 12 10 12 6 C12 2.6 9.3 0 6 0Z" fill="#fff"/><circle cx="6" cy="6" r="2.2" fill="#f47a20"/></svg>
      <div class="address">Halvera Fitness<br>Main Street 418 Birchwood<br>Ave North Elmford</div>
      <svg width="13" height="13" viewBox="0 0 13 13" style="left:190px;top:114px"><path d="M3 0 L5 4 L3.5 5.5 Q5 8.5 7.5 9.5 L9 8 L13 10 L12 13 Q3 12 0 2 Z" fill="#fff"/></svg>
      <svg width="14" height="11" viewBox="0 0 14 11" style="left:190px;top:143px"><rect width="14" height="11" fill="#fff"/><path d="M0 0 L7 6 L14 0" fill="none" stroke="#f47a20"/></svg>
      <div class="reach">+1 (555) 014-2290<br>hello@halverafit.com</div>
      <div class="social"><i></i><i></i><i></i></div>
    </div>
  </div>
</section>

<footer class="section footer">
  <nav><a class="active" href="#">Home</a><a href="#">About Us</a><a href="#">Training</a><a href="#">Classes</a><a href="#">Contact Us</a><a href="#">Testimonials</a></nav>
  <div class="copy">© 2016 - www.halverafit.com</div>
</footer>

</body>
</html>
```